Gilt Corner Shop Sign

Name of company
Gilt Corner
Gilt Corner is a picture framing shop and art gallery selling custom frames, art work and gifts.
Needing a design for shop front sign.

The Sign
The sign is above the shop front window and is approximately 12 feet wide by 43 inches high. White on black. White striped boarder that looks like a picture frame with Gilt Corner in classic lettering including space for a phone number and it may or may not need to include description of services. Something cute in one area like a picture frame with a heart inside. A friendly feel like something that would be special and feels like yours. I have attached a photo of the existing sign to be replaced.

Thank you for your time.

```html
<!DOCTYPE html>
<html lang="en">
<head>
<meta charset="utf-8">
<title>Gilt Corner – Shop Sign</title>
<link rel="stylesheet" href="https://fonts.googleapis.com/css2?family=Cormorant+Garamond:ital,wght@0,500;0,600;1,500&display=swap">
<style>
  :root {
    --backdrop: #e9e7e3;
    --sign-black: #1f1f21;
    --sign-white: #f6f5f2;
  }
  * { margin: 0; padding: 0; box-sizing: border-box; }
  html, body {
    width: 1200px;
    height: 923px;
    overflow: hidden;
    background: var(--backdrop);
  }
  .canvas {
    position: relative;
    width: 1200px;
    height: 923px;
    display: flex;
    align-items: center;
    justify-content: center;
  }
  .shop-sign {
    position: relative;
    width: 1100px;
    height: 330px;
    background: var(--sign-black);
    box-shadow: 0 6px 18px rgba(0,0,0,0.18);
  }
  .frame-border {
    position: absolute;
    inset: 0;
    width: 100%;
    height: 100%;
  }
  .sign-content {
    position: absolute;
    inset: 0;
    font-family: "Cormorant Garamond", "Times New Roman", serif;
    color: var(--sign-white);
  }
  .shop-name {
    position: absolute;
    left: 0;
    right: 0;
    top: 88px;
    text-align: center;
    font-weight: 600;
    font-size: 118px;
    line-height: 1;
    letter-spacing: 0.14em;
    text-transform: uppercase;
  }
  .contact-row {
    position: absolute;
    right: 118px;
    top: 218px;
    display: flex;
    align-items: center;
    gap: 18px;
  }
  .heart-frame {
    width: 44px;
    height: 44px;
    flex: none;
  }
  .shop-phone {
    font-weight: 600;
    font-size: 38px;
    line-height: 1;
    letter-spacing: 0.03em;
    font-variant-numeric: lining-nums;
  }
</style>
</head>
<body>
<main class="canvas">
  <section class="shop-sign" aria-label="Gilt Corner shop front sign">
    <svg class="frame-border" viewBox="0 0 1100 330" aria-hidden="true">
      <defs>
        <pattern id="diagonal-stripes" width="9" height="9" patternUnits="userSpaceOnUse" patternTransform="rotate(45)">
          <rect width="9" height="9" fill="#1f1f21"/>
          <rect width="3.5" height="9" fill="#f6f5f2"/>
        </pattern>
      </defs>
      <rect x="16" y="16" width="1068" height="298" fill="url(#diagonal-stripes)"/>
      <rect x="30" y="30" width="1040" height="270" fill="#1f1f21"/>
      <rect x="16" y="16" width="1068" height="298" fill="none" stroke="#f6f5f2" stroke-width="1.5"/>
      <rect x="30" y="30" width="1040" height="270" fill="none" stroke="#f6f5f2" stroke-width="1.5"/>
    </svg>
    <div class="sign-content">
      <h1 class="shop-name">Gilt Corner</h1>
      <div class="contact-row">
        <svg class="heart-frame" viewBox="0 0 44 44" role="img" aria-label="Small picture frame with a heart inside">
          <rect x="2" y="2" width="40" height="40" fill="none" stroke="#f6f5f2" stroke-width="3"/>
          <rect x="8" y="8" width="28" height="28" fill="none" stroke="#f6f5f2" stroke-width="1.5"/>
          <path d="M22 30 C14 24 12 20.5 12 17.5 C12 14.8 14 13 16.4 13 C18.6 13 20.6 14.4 22 16.6 C23.4 14.4 25.4 13 27.6 13 C30 13 32 14.8 32 17.5 C32 20.5 30 24 22 30 Z" fill="#f6f5f2"/>
        </svg>
        <p class="shop-phone">T: 01632 960415</p>
      </div>
    </div>
  </section>
</main>
</body>
</html>
```